Real Estate "For Sale" Sign for construction company

We need a sign that we can use to hang on a post and place on the road when we sell a property. The sign will be simple and will need to mainly feature our logo (files attached), as well as the words "For Sale", and then our phone number "(555) 617 3489". The sign will hang on a post that'll look something like the attached picture.

Target Market(s)

Home buyers

Industry/Entity Type

Real Estate

Font styles to use
Serif
Sans Serif

Colors
0054AA
0677BA
7BADD7
CADEEF
E8F1F8
0094D4
00A9DD
6FCCEA
C7EBF8
E9F6FB

Requirements
Must have
• For Sale & our phone number

```html
<!DOCTYPE html>
<html lang="en">
<head>
<meta charset="utf-8">
<title>For Sale Sign</title>
<link rel="stylesheet" href="https://fonts.googleapis.com/css2?family=Poppins:wght@400;800;900&display=swap">
<style>
  :root {
    --navy: #14204a;
    --brand-blue: #1b7cc1;
    --panel-white: #ffffff;
    --backdrop-light: #fafafa;
    --backdrop-dark: #e2e3e5;
  }
  html, body {
    margin: 0;
    padding: 0;
    width: 1200px;
    height: 1097px;
    overflow: hidden;
  }
  body {
    background: linear-gradient(90deg, var(--backdrop-light), var(--backdrop-dark));
    font-family: "Poppins", sans-serif;
  }
  .sale-sign {
    position: absolute;
    left: 117px;
    top: 210px;
    width: 966px;
    height: 678px;
  }
  .sign-body { fill: var(--navy); }
  .sign-band { fill: var(--panel-white); }
  .house-icon { fill: var(--brand-blue); }
  .house-door { fill: var(--navy); }
  .brand-name {
    font-family: "Poppins", sans-serif;
    font-weight: 400;
    font-size: 21px;
    fill: var(--brand-blue);
  }
  .headline {
    font-family: "Poppins", sans-serif;
    font-weight: 900;
    font-size: 121px;
    fill: var(--brand-blue);
  }
  .call-line {
    font-family: "Poppins", sans-serif;
    font-weight: 800;
    font-size: 40px;
  }
  .call-label { fill: var(--navy); }
  .call-number { fill: var(--brand-blue); }
</style>
</head>
<body>
  <svg class="sale-sign" viewBox="0 0 690 484" xmlns="http://www.w3.org/2000/svg" role="img" aria-label="For Sale sign, Blue Ridge Hollow Realty, call (555) 617 3489">
    <path class="sign-body" d="M20,0 H555 Q565,0 571,11 L684,228 Q690,240 684,252 L571,471 Q565,482 555,482 H20 Q0,482 0,462 V20 Q0,0 20,0 Z"/>
    <polygon class="sign-band" points="18,25 553,25 609,131 18,131"/>
    <polygon class="sign-band" points="18,372 599,372 555,457 18,457"/>

    <text class="brand-name" x="313" y="100" text-anchor="middle">Blue Ridge Hollow Realty</text>

    <g class="house-icon">
      <polygon points="44,231 121,154 198,231 180,231 121,172 62,231"/>
      <polygon points="66,236 121,183 178,236 178,340 66,340"/>
    </g>
    <g class="house-door">
      <circle cx="121" cy="247" r="15"/>
      <rect x="99" y="262" width="46" height="78"/>
    </g>
    <circle class="house-icon" cx="121" cy="247" r="7"/>

    <text class="headline" x="228" y="240" textLength="255" lengthAdjust="spacingAndGlyphs">FOR</text>
    <text class="headline" x="226" y="342" textLength="315" lengthAdjust="spacingAndGlyphs">SALE</text>

    <text class="call-line" x="53" y="427" textLength="473" lengthAdjust="spacingAndGlyphs"><tspan class="call-label">CALL : </tspan><tspan class="call-number">(555) 617 3489</tspan></text>
  </svg>
</body>
</html>
```